Driving-coach/trainer who wants to inform about the offer and how I can help people to drive more re

I need a flyer that informs potential customers about my offer.

DL size 210 mm x 99 mm, vertical!

I'm a trainer/coach who helps people to drive a car more relaxed, without fear and more confident.

It's a one to one training. I do train people in their own car. It gets people their freedom back to go where and when they like to go by own car...

Target Market(s)

People (man an woman) who are afraid of driving a car, or are very stressed while driving....

Industry/Entity Type

Life Coaching

Font styles to use
Sans Serif

Colors
acd136

Requirements
Must have
• Page 1:
• -my offer (see text-pdf)
• -three fotos (see attached files "Pixmarra") of people who are satisfied with my offer
• Page 2:
• -advantages in the work with me.
• -contact information
• -and a picture of me (see attached file) next to the contact information or the advantages of my work
• -my logo (see attached file) on Page 1 + 2
• -i like a "clear" and structured layout. "Less is more"

```html
<!DOCTYPE html>
<html lang="de">
<head>
<meta charset="utf-8">
<title>Fahrangst erfolgreich überwinden – Flyer</title>
<link rel="stylesheet" href="https://fonts.googleapis.com/css2?family=Nunito:wght@700;800;900&family=Open+Sans:wght@300;400;600&family=Didact+Gothic&display=swap">
<style>
  :root{
    --green:#acd136;
    --green-dark:#8fb024;
    --ink:#2b2b2d;
    --paper:#ececec;
    --text:#333;
    --stage:#d9d9d9;
  }
  *{box-sizing:border-box;margin:0;padding:0}
  html,body{width:1200px;height:1200px;overflow:hidden;background:var(--stage)}
  .canvas{position:relative;width:1200px;height:1200px}
  .flyer{position:absolute;top:59px;width:510px;height:1082px;background:var(--paper);overflow:hidden;
    font-family:"Open Sans",sans-serif;color:var(--text);box-shadow:0 6px 18px rgba(0,0,0,.25)}
  .flyer--front{left:60px}
  .flyer--back{left:630px}
  .abs{position:absolute}
  .photo{position:absolute;left:0;top:0;width:510px}
  .photo--driver{height:360px;background:linear-gradient(135deg,#5b5f63 0%,#8c8f92 30%,#c79a6b 55%,#b98552 75%,#e6e1d8 100%)}
  .photo--happy{height:350px;background:linear-gradient(120deg,#6d7f5c 0%,#b9c3c9 35%,#e4c2a4 55%,#9fa8b0 80%,#d9dee2 100%)}
  .wave{position:absolute;left:0;width:510px}
  .title-tag{position:absolute;background:var(--green);color:#fff;font-family:"Open Sans",sans-serif;font-weight:400;
    text-transform:uppercase;font-size:26px;line-height:27px;padding:16px 14px 18px 16px;transform:rotate(-3deg)}
  .flyer--back .title-tag{transform:rotate(3deg)}
  .badge{position:absolute;left:345px;top:272px;width:112px;height:112px;border-radius:50%;background:#fff;border:5px solid var(--green);
    display:flex;align-items:center;justify-content:center;text-align:center;font-family:"Nunito",sans-serif;font-weight:800;
    font-size:14px;line-height:14px;color:var(--ink)}
  .heading{font-family:"Nunito",sans-serif;font-weight:900;color:var(--green)}
  .front-heading{left:120px;top:370px;font-size:34px}
  .questions{left:90px;top:438px;list-style:none;font-family:"Nunito",sans-serif;font-weight:800;font-size:17px;color:var(--ink)}
  .questions li{margin-bottom:6px}
  .questions li::before{content:"»";color:var(--green);margin-right:10px;font-size:18px}
  .banner{left:0;top:528px;width:450px;height:56px}
  .banner-text{left:72px;top:540px;font-family:"Nunito",sans-serif;font-weight:900;font-size:22px;color:#fff;display:flex;align-items:center;gap:10px}
  .banner-text::before{content:"";width:16px;height:16px;background:#fff;display:inline-block}
  .situations-lead{left:90px;top:598px;font-size:21px;line-height:24px;color:var(--ink)}
  .checks{list-style:none;position:absolute}
  .checks li{position:relative;padding-left:30px;font-size:11px;line-height:14px;color:var(--text)}
  .checks li::before{content:"";position:absolute;left:0;top:0;width:20px;height:20px;border-radius:50%;background:var(--green)}
  .checks li::after{content:"";position:absolute;left:6px;top:4px;width:8px;height:5px;border-left:2.5px solid #fff;border-bottom:2.5px solid #fff;transform:rotate(-45deg)}
  .hl{color:var(--green-dark)}
  .checks--front{left:60px;top:662px;width:440px}
  .checks--front li{margin-bottom:18px}
  .cheer{left:0;width:510px;top:880px;text-align:center;font-family:"Nunito",sans-serif;font-weight:900;font-size:21px;line-height:20px;color:var(--green)}
  .coach-name{font-family:"Didact Gothic",sans-serif;color:var(--green);letter-spacing:2px}
  .front-name{left:55px;top:1010px;font-size:26px}
  .front-role{left:55px;top:1044px;font-size:16px;letter-spacing:2.5px}
  .steps-heading{left:0;width:510px;top:336px;text-align:center;font-size:29px}
  .step{position:absolute;top:395px;width:112px;height:112px;border-radius:50%;background:var(--ink);border:6px solid var(--green);
    display:flex;align-items:center;justify-content:center;text-align:center;font-family:"Nunito",sans-serif;font-weight:800;color:var(--green);padding:8px}
  .step-num{position:absolute;left:-18px;top:-22px;width:46px;height:46px;border-radius:50%;background:#fff;border:5px solid var(--green);
    font-family:"Nunito",sans-serif;font-weight:900;font-size:24px;color:var(--ink);display:flex;align-items:center;justify-content:center}
  .step--1{left:45px;font-size:17px;line-height:16px}
  .step--2{left:195px;font-size:11px;line-height:11px}
  .step--3{left:345px;font-size:12px;line-height:12px}
  .adv-heading{left:0;width:510px;top:530px;text-align:center;font-size:24px}
  .tab{position:absolute;top:532px;width:36px;height:36px;background:var(--green)}
  .tab--left{left:0;clip-path:polygon(0 0,75% 0,100% 50%,75% 100%,0 100%)}
  .tab--right{right:0;clip-path:polygon(25% 0,100% 0,100% 100%,25% 100%,0 50%)}
  .checks--back{left:40px;top:592px;width:440px}
  .checks--back li{margin-bottom:16px;font-size:11.5px;line-height:15px}
  .portrait{left:335px;top:790px;width:155px;height:220px;border-radius:78px 78px 0 0;background:linear-gradient(180deg,#cdbfb2 0%,#f3f3f3 45%,#ffffff 100%)}
  .contact-name{left:45px;top:832px;font-family:"Nunito",sans-serif;font-weight:900;font-size:21px;color:var(--ink)}
  .contact-more{left:45px;top:860px;font-family:"Nunito",sans-serif;font-weight:800;font-size:13px;color:var(--green-dark)}
  .contact-web{left:45px;top:885px;font-family:"Nunito",sans-serif;font-weight:800;font-size:12px;color:var(--green-dark);display:flex;align-items:center;gap:6px}
  .call-lead{left:40px;top:1012px;font-family:"Nunito",sans-serif;font-weight:800;font-size:14px;color:var(--green)}
  .call-phone{left:40px;top:1034px;font-family:"Nunito",sans-serif;font-weight:900;font-size:23px;color:var(--green);display:flex;align-items:center;gap:8px}
</style>
</head>
<body>
<div class="canvas">

  <!-- Page 1 -->
  <section class="flyer flyer--front">
    <div class="photo photo--driver" role="img" aria-label="Foto: zufriedene Fahrerin im Cabrio am Lenkrad"></div>
    <svg class="wave" style="top:250px" width="510" height="140" viewBox="0 0 510 140">
      <path d="M0 140 L0 120 Q120 20 280 70 Q420 110 510 20 L510 140 Z" fill="var(--paper)"/>
      <path d="M30 120 Q160 40 300 70 Q200 60 30 120 Z" fill="var(--green)"/>
      <path d="M400 80 Q470 50 510 0 L510 30 Q470 70 400 80 Z" fill="var(--green)"/>
    </svg>
    <div class="title-tag" style="left:22px;top:32px">Fahrangst<br>erfolgreich<br>überwinden!</div>
    <div class="badge">ICH<br>HABS<br>GESCHAFF!!</div>

    <h2 class="abs heading front-heading">Wollen Sie</h2>
    <ul class="abs questions">
      <li>Fahrangst überwinden?</li>
      <li>Panikattacken beim Autofahren loswerden?</li>
      <li>Sicher und entspannt Autofahren?</li>
    </ul>

    <svg class="abs banner" width="450" height="56" viewBox="0 0 450 56">
      <polygon points="0,10 450,0 438,50 0,56" fill="var(--green-dark)"/>
      <polygon points="0,6 440,0 428,46 0,50" fill="var(--green)"/>
    </svg>
    <div class="abs banner-text">Dann sind Sie hier richtig!</div>

    <p class="abs situations-lead">Kommt Ihnen eine dieser Situationen<br>bekannt vor?</p>
    <ul class="checks checks--front">
      <li>Autofahren erleben Sie unter hoher Anspannung und Stress. - Sie wünschen sich, Autofahren <span class="hl">sicher und entspannt</span> zu erleben.</li>
      <li>Bestimmte Situationen (z.B. unbekannte Strecken, Autobahn, Baustellen, Stadtverkehr, Parken…) bereiten Ihnen großen Stress oder trauen Sie sich nicht zu. - Sie möchten diese Situationen <span class="hl">gelassener und souveräner</span> meistern.</li>
      <li>Sie fühlen sich durch andere Verkehrsteilnehmer gestresst und unter Druck. Sie haben Angst auf unvorhergesehene Situationen nicht richtig reagieren zu können. - Sie möchten <span class="hl">Autofahren entspannter und souveräner erleben.</span></li>
      <li>Angst oder Panikattacken begleiten Sie beim Autofahren. Vielleicht vermeiden Sie deshalb das Autofahren komplett. - Sie möchten <span class="hl">angstfrei und entspannt Auto fahren.</span></li>
    </ul>
    <p class="abs cheer">Auch Sie<br>Können<br>es schaffen!!</p>

    <svg class="wave" style="top:940px" width="510" height="142" viewBox="0 0 510 142">
      <path d="M0 142 L0 100 Q80 40 200 55 Q380 80 510 10 L510 142 Z" fill="var(--ink)"/>
      <path d="M0 90 Q60 30 140 36 Q60 46 0 110 Z" fill="var(--green)"/>
      <path d="M260 57 Q400 62 510 0 L510 14 Q400 78 260 57 Z" fill="var(--green)"/>
    </svg>
    <div class="abs coach-name front-name">Sabine Kellerhoff</div>
    <div class="abs coach-name front-role">Fahrangst-Bewältigungs-Coach</div>
  </section>

  <!-- Page 2 -->
  <section class="flyer flyer--back">
    <div class="photo photo--happy" role="img" aria-label="Foto: lächelnde Fahrerin im Autofenster mit Daumen hoch"></div>
    <svg class="wave" style="top:230px" width="510" height="130" viewBox="0 0 510 130">
      <path d="M0 130 L0 40 Q90 120 250 90 Q400 60 510 110 L510 130 Z" fill="var(--paper)"/>
      <path d="M0 10 Q40 90 120 110 Q40 110 0 60 Z" fill="var(--green)"/>
      <path d="M300 70 Q420 50 500 120 Q420 80 300 70 Z" fill="var(--green)"/>
    </svg>
    <div class="title-tag" style="left:32px;top:22px">Fahrangst<br>erfolgreich<br>überwinden!</div>

    <h2 class="abs heading steps-heading">3 Schritte zur Lösung:</h2>
    <div class="step step--1"><span class="step-num">1</span>Erstge-<br>spräch<br>verein-<br>baren</div>
    <div class="step step--2"><span class="step-num">2</span>Analyse<br>Ihrer<br>individuellen<br>Situation<br>und<br>Zielsetzung</div>
    <div class="step step--3"><span class="step-num">3</span>Individuelles<br>Coaching<br>und<br>Training</div>

    <div class="tab tab--left"></div>
    <div class="tab tab--right"></div>
    <h2 class="abs heading adv-heading">Advantages in the work with me:</h2>
    <ul class="checks checks--back">
      <li>Über 10 Jahre Erfahrung als Trainerin und Coach im Bereich Fahrsicherheit</li>
      <li>Als psychotherapeutische Heilpraktikerin bin ich auf Angststörungen und Panikattacken spezialisiert</li>
      <li>100 % auf Sie zugeschnitten: ich hole Sie genau dort ab, wo Sie jetzt stehen und unterstütze Sie in Ihrem Prozess individuell und zielführend.</li>
      <li>Termine sind auch abends und am Wochenende möglich</li>
      <li>Wenn es Ihnen nicht möglich ist, in meine Praxis nach Lindenfeld Nord zu kommen: Mit der mobilen Praxis komme ich auch zu Ihnen</li>
    </ul>

    <div class="abs portrait" role="img" aria-label="Porträtfoto der Trainerin"></div>
    <svg class="wave" style="top:880px" width="510" height="202" viewBox="0 0 510 202">
      <path d="M0 202 L0 20 Q60 10 100 60 Q170 140 300 110 Q420 80 510 140 L510 202 Z" fill="var(--ink)"/>
      <path d="M40 10 Q90 20 130 80 Q180 125 280 112 Q170 142 110 88 Q80 40 40 10 Z" fill="var(--green)"/>
      <path d="M430 100 Q480 110 510 140 L510 150 Q480 120 430 100 Z" fill="var(--green)"/>
    </svg>
    <div class="abs contact-name">Sabine Kellerhoff</div>
    <div class="abs contact-more">Weitere Informationen finden Sie auf:</div>
    <div class="abs contact-web">
      <svg width="16" height="16" viewBox="0 0 16 16" fill="none" stroke="var(--green-dark)" stroke-width="1.3"><circle cx="8" cy="8" r="6.5"/><ellipse cx="8" cy="8" rx="3" ry="6.5"/><line x1="1.5" y1="8" x2="14.5" y2="8"/></svg>
      www.fahrsicher-coaching-beispiel.de
    </div>
    <div class="abs call-lead">Oder rufen Sie mich einfach an:</div>
    <div class="abs call-phone">
      <svg width="24" height="24" viewBox="0 0 24 24"><rect width="24" height="24" rx="3" fill="var(--green)"/><path d="M8 5 L10 9 L8.5 10.5 Q10 14 13.5 15.5 L15 14 L19 16 L18 19 Q10 19 5 10 Z" fill="var(--ink)"/></svg>
      0151 00 47 31 86
    </div>
  </section>

</div>
</body>
</html>
```